PREMIUM AGENCY High End Business Card - A+++ Designers Wanted

** DO NOT ATTEMPT TO CONTACT ME THROUGH SEARCHING ON ZINTREL OR EMAILING ME THROUGH MY WEBSITE **

I need a fresh, contemporary business card designed using the logo attached (BRONSALK)

I have attached the font for BRONSALK

It must have a premium look and feel. The business card size must be STANDARD size.

You can submit either/both VERTICAL or HORIZONTAL designs.

FRONT: It must have the following sample information on

Paul Ardley
Director Operations
Mobile +61 452 118 906
Email paulardley@bronsalk.com
www.bronsalk.com

The REAR of the business card must have the words

CREATE INSPIRE TOMORROW

as part of the design, in the same font (NEXA) attached.

The words do not need to be in capitals, or on the same line, please design this as you see it best working.

ADDITIONAL INFORMATION
======================

The BRONSALK logo must be on the front of the card

I want Ultraviolet printing on the final design, to enhance either the NAME of the person OR the BRONSALK logo OR the words on the back of the card.

Target Market(s)

Agency, Advertising Agency, Creative, Designers

Industry/Entity Type

Media

Contact Information for Business Card

Design Agency, Contemporary, Premium look and feel, High Quality

Font styles to use
Serif
Sans Serif
Other font styles liked:
• ATTACHED TO PROJECT

Requirements
Must have
• BLACK & WHITE as the primary design, and if you feel there can be a highlighted colour, then this can be used.
• The Logo ICON attached is blue, this colour must not be changed.
• I have attached the partner brand BRONSALK MEDIA incase you need to manipulate the original files.
• ** DO NOT ATTEMPT TO CONTACT ME THROUGH SEARCHING ON ZINTREL OR EMAILING ME THROUGH MY WEBSITE **
Nice to have
• Must be Premium. I have attached some sample designs, that I like that would be a good inspiration for where this can be taken.
• My favourite design is is the KESTRAVUE2-BUSINESSCARD-TEMPLATE
Should not have
• No funny or silly standard / off the shelf designs

```html
<!DOCTYPE html>
<html lang="en">
<head>
<meta charset="utf-8">
<title>Bronsalk Media – Business Card</title>
<link rel="stylesheet" href="https://fonts.googleapis.com/css2?family=Lexend+Zetta:wght@200&family=Quicksand:wght@300&display=swap">
<style>
  :root {
    --card-base: #f3f3f3;
    --tile-light: #f8f8f8;
    --tile-mid: #ececec;
    --tile-dark: #e2e2e2;
    --ink-grey: #7b7b7b;
    --tagline-grey: #8a8a8a;
    --brand-blue: #3aa8e0;
  }
  html, body {
    margin: 0;
    padding: 0;
    width: 1200px;
    height: 722px;
    overflow: hidden;
    background: var(--card-base);
  }
  .card {
    position: relative;
    width: 1200px;
    height: 722px;
    overflow: hidden;
    background: var(--card-base);
    font-family: "Quicksand", "Helvetica Neue", Arial, sans-serif;
  }
  .card__texture {
    position: absolute;
    inset: 0;
    background:
      linear-gradient(135deg, var(--tile-mid) 0%, var(--tile-light) 35%, var(--tile-mid) 55%, var(--tile-light) 80%, var(--tile-dark) 100%);
  }
  .card__tagline {
    position: absolute;
    left: 0;
    top: 0;
    width: 1200px;
    height: 722px;
  }
  .card__tagline text {
    font-family: "Lexend Zetta", "Helvetica Neue", Arial, sans-serif;
    font-weight: 200;
    font-size: 40px;
    fill: var(--tagline-grey);
  }
  .brand {
    position: absolute;
    left: 150px;
    top: 330px;
    width: 210px;
    display: flex;
    flex-direction: column;
    align-items: center;
    gap: 18px;
  }
  .brand__dot {
    width: 44px;
    height: 44px;
    border-radius: 50%;
    background: var(--brand-blue);
  }
  .brand__name {
    font-weight: 300;
    font-size: 38px;
    letter-spacing: 1px;
    color: var(--brand-blue);
    line-height: 1;
  }
  .contact {
    margin: 0;
    padding: 0;
    list-style: none;
  }
  .contact__line {
    position: absolute;
    left: 496px;
    font-weight: 300;
    font-size: 55px;
    line-height: 1;
    color: var(--ink-grey);
    white-space: nowrap;
  }
  .contact__line--name  { top: 198px; }
  .contact__line--role  { top: 281px; }
  .contact__line--phone { top: 364px; }
  .contact__line--email { top: 447px; }
  .contact__line--web   { top: 528px; }
</style>
</head>
<body>
  <main class="card">
    <div class="card__texture" role="img" aria-label="Faint grey diamond tile texture across the card"></div>

    <svg class="card__tagline" viewBox="0 0 1200 722" aria-label="Create Inspire Tomorrow">
      <text x="94" y="139" textLength="1010" lengthAdjust="spacingAndGlyphs">CREATE INSPIRE TOMORROW</text>
    </svg>

    <div class="brand">
      <span class="brand__dot"></span>
      <span class="brand__name">BRONSALK</span>
    </div>

    <ul class="contact">
      <li class="contact__line contact__line--name">Paul Ardley</li>
      <li class="contact__line contact__line--role">Director Operations</li>
      <li class="contact__line contact__line--phone">+61 452 118 906</li>
      <li class="contact__line contact__line--email">paulardley@bronsalk.com</li>
      <li class="contact__line contact__line--web">www.bronsalk.com</li>
    </ul>
  </main>
</body>
</html>
```